Brochure Cover and Back pages

We are a US-based cosmetics company that sells state-of-the-art skin care products, including advanced anti-aging serums, natural mineral sunscreens, organic antioxidant moisturizers, and organic face cleansers. We need a product brochure. We already have chosen a design for the layout of the product info pages. But we still need a cover page and a back page. We are looking for simple but elegant design for the cover page. The back page is less important and we already know what we want on the back page. It will be the company's mission statement and at the bottom, the company URL, phone number, etc.

The brochure has two folds. So there will be three panels on both sides. The size of each panel is 16.5 (l) x 9.5 (w) cm.

At the end of the project, we expect the designer to integrate all the pages so that the finished copy is read to be sent off to a printing service for printing.

All the product info pages are attached. Also attached are the text (info) to go on the back page, company logo with and without the tagline, the icon in the logo.

YOu are welcome to visit our website www.morvask.com to learn about our products.

Industry/Entity Type

Cosmetics

```html
<!DOCTYPE html>
<html lang="en">
<head>
<meta charset="utf-8">
<title>Morvask Brochure – Cover and Back Panels</title>
<link rel="stylesheet" href="https://fonts.googleapis.com/css2?family=Advent+Pro:wght@200&family=Arimo:wght@400&family=Lato:wght@400;700&family=Open+Sans:wght@400&display=swap">
<style>
  :root {
    --page: #ffffff;
    --frame: #555555;
    --pink-soft: #fbe3ec;
    --pink-mid: #f7cedd;
    --pink-mark: #f6b2a8;
    --grey-text: #666666;
    --grey-quote: #9a9a9a;
    --grey-name: #6d6d6f;
    --ink: #1a1a1a;
    --card-border: #8fc8e0;
    --card-shade: #ebebeb;
    --product-border: #f2a9bf;
    --tube: #eef1f4;
    --navy-thin: #3e5878;
    --navy: #1d4a72;
  }
  * { margin: 0; padding: 0; box-sizing: border-box; }
  html, body { width: 1200px; height: 1001px; overflow: hidden; background: var(--page); }
  .canvas {
    position: relative; width: 1200px; height: 1001px;
    border: 1px solid var(--frame); background: var(--page);
  }
  .spread {
    position: absolute; left: 62px; top: 190px; width: 1080px; height: 624px;
    border: 1px solid var(--frame); overflow: hidden;
  }
  .spread-backdrop {
    position: absolute; inset: 0;
    background:
      radial-gradient(ellipse at 78% 45%, var(--pink-mid) 0%, rgba(247,206,221,0) 55%),
      radial-gradient(ellipse at 40% 80%, var(--pink-mid) 0%, rgba(247,206,221,0) 50%),
      linear-gradient(90deg, var(--pink-soft), #fdf0f5 50%, var(--pink-soft));
  }
  .panel { position: absolute; top: 0; height: 100%; }

  /* Product panel */
  .panel-products { left: 0; width: 360px; }
  .section-title { position: absolute; left: 9px; top: 5px; font: 400 18px/1.1 "Open Sans", sans-serif; color: var(--grey-text); }
  .section-sub { position: absolute; left: 9px; top: 30px; font: 400 11px/1 "Open Sans", sans-serif; color: var(--grey-text); }
  .product-card {
    position: absolute; left: 7px; width: 351px; height: 155px;
    border: 1px solid var(--card-border); border-radius: 9px; background: #fff;
  }
  .product-card.shaded { background: var(--card-shade); }
  .product-card h3 { position: absolute; left: 13px; top: 24px; font: 700 13px/1 "Lato", sans-serif; color: var(--ink); }
  .product-card p { position: absolute; left: 13px; top: 50px; width: 232px; font: 400 12px/17px "Lato", sans-serif; color: var(--ink); }
  .product-tube {
    position: absolute; right: 22px; top: 10px; width: 54px; height: 138px;
    border-radius: 6px 6px 3px 3px;
    background: linear-gradient(90deg, #dfe4ea, var(--tube) 40%, #fff 60%, #dde3ea);
  }
  .contact-line { position: absolute; left: 49px; top: 598px; font: 400 14px/1 "Arimo", sans-serif; letter-spacing: 1.6px; color: var(--grey-text); }

  /* Back panel */
  .panel-back { left: 360px; width: 360px; }
  .mission-quote { position: absolute; left: 36px; top: 56px; font: 400 38px/48px "Arimo", sans-serif; color: var(--grey-quote); }
  .brand { position: absolute; left: 0; width: 100%; text-align: center; }
  .brand-mark { display: block; margin: 0 auto; background: var(--pink-mark); }
  .brand-name { display: block; font-family: "Arimo", sans-serif; font-weight: 400; color: var(--grey-name); }
  .brand-tagline { display: block; font: 400 12px/1 "Lato", sans-serif; color: var(--grey-text); letter-spacing: .4px; }
  .panel-back .brand { top: 252px; left: -10px; }
  .panel-back .brand-mark { width: 56px; height: 56px; }
  .panel-back .brand-name { font-size: 84px; line-height: 100px; }
  .panel-back .brand-tagline { margin-top: 4px; }
  .back-url { position: absolute; left: 0; width: 100%; text-align: center; top: 556px; font: 400 28px/1 "Arimo", sans-serif; letter-spacing: 4px; color: var(--grey-text); }

  /* Cover panel */
  .panel-cover { left: 720px; width: 360px; }
  .panel-cover .brand { top: 12px; left: 16px; }
  .panel-cover .brand-mark { width: 34px; height: 34px; }
  .panel-cover .brand-name { font-size: 70px; line-height: 84px; }
  .panel-cover .brand-tagline { margin-top: 6px; }
  .product-lineup {
    position: absolute; left: 28px; top: 193px; width: 308px; height: 156px;
    border: 1px solid var(--product-border); border-radius: 9px; background: #fff;
  }
  .lineup-item { position: absolute; background: linear-gradient(90deg, #e2e6ea, #f6f7f9 50%, #e0e4e8); }
  .cover-quote { position: absolute; left: 0; width: 100%; text-align: center; top: 384px; padding-left: 12px; font: 200 39px/47px "Advent Pro", sans-serif; letter-spacing: 1px; color: var(--navy-thin); }
  .cover-url { position: absolute; left: 68px; top: 582px; font: 400 26px/1 "Arimo", sans-serif; letter-spacing: 3px; color: var(--navy); }
</style>
</head>
<body>
<div class="canvas">
  <div class="spread">
    <div class="spread-backdrop" role="img" aria-label="Soft pink floral background wash"></div>

    <section class="panel panel-products">
      <h2 class="section-title">Organic Face Cleansers</h2>
      <p class="section-sub">Gentle for All Skin Types</p>

      <article class="product-card" style="top:62px">
        <h3>Refreshing Natural Cleanser</h3>
        <p>This refreshing aloe-based gel cleanser is formulated with organic ingredients. It cleans thoroughly without drying out the skin. Balances skin hydration and sebum.&nbsp; 4 fl. oz.</p>
        <div class="product-tube" role="img" aria-label="Product photo: Refreshing Natural Cleanser tube"></div>
      </article>

      <article class="product-card shaded" style="top:246px">
        <h3>Hydrating Organic Cleanser</h3>
        <p>This light gel cleanser is formulated with coconut milk and honey for a moisturizing wash. Gently washes away dirt and oil, leaving skin hydrated and softened.&nbsp; 4 fl. oz.</p>
        <div class="product-tube" role="img" aria-label="Product photo: Hydrating Organic Cleanser tube"></div>
      </article>

      <article class="product-card" style="top:436px">
        <h3>Nourishing Cleansing Milk</h3>
        <p>This comforting organic lotion cleanser is enriched with botanical extracts to leave skin feeling smooth and soft. Can be used to remove eye makeup.&nbsp; 4 fl. oz.</p>
        <div class="product-tube" role="img" aria-label="Product photo: Nourishing Cleansing Milk tube"></div>
      </article>

      <p class="contact-line">www.morvask.com&nbsp;&nbsp; 1-855-555-0142</p>
    </section>

    <section class="panel panel-back">
      <p class="mission-quote">“Creating Beauty<br>Solutions through<br>Science”</p>
      <div class="brand">
        <span class="brand-mark"></span>
        <span class="brand-name">Morvask</span>
        <span class="brand-tagline">Bringing You Smart Skin Care</span>
      </div>
      <p class="back-url">www.morvask.com</p>
    </section>

    <section class="panel panel-cover">
      <div class="brand">
        <span class="brand-mark"></span>
        <span class="brand-name">Morvask</span>
        <span class="brand-tagline">Bringing You Smart Skin Care</span>
      </div>
      <div class="product-lineup">
        <div class="lineup-item" style="left:38px;top:8px;width:46px;height:136px;border-radius:8px 8px 3px 3px" role="img" aria-label="Product photo: skin recovery serum bottle"></div>
        <div class="lineup-item" style="left:128px;top:6px;width:62px;height:142px;border-radius:5px 5px 2px 2px" role="img" aria-label="Product photo: brightening cream tube"></div>
        <div class="lineup-item" style="left:234px;top:6px;width:44px;height:140px;border-radius:14px 14px 4px 4px" role="img" aria-label="Product photo: clarifying liquid bottle"></div>
      </div>
      <p class="cover-quote">“Creating Beauty<br>Solutions<br>through Science”</p>
      <p class="cover-url">www.morvask.com</p>
    </section>
  </div>
</div>
</body>
</html>
```